QM Interiors needs and Interior Design Business card

I can do anything from Commercial to Residential and Free lance. Beginning to end in design selection process.
Need something to catch the eye of potential customers and vendors. From furniture to Tile and Cabinet selections. I can do it all.

Industry/Entity Type

Design Agency

Contact Information for Business Card

QM Interiors- Design Consultanting Residential, Commerical
Maybe a cool detail background. Wall paper print that can have some texture

Font styles to use
Serif

Colors
709dcb
34a6d7
b868aa
e667a6
f59296
85acd3
ffffff
000000
5c5c5c

Requirements
Must have
• Square or Rectangular with Rounded edges
• Name
• Address
• Phone
• Email
Nice to have
• Some colored edges More simples not too busy
• Pattern detail in background.
Should not have
• Not too much color

```html
<!DOCTYPE html>
<html lang="en">
<head>
<meta charset="utf-8">
<title>QM Interiors — Business Card</title>
<link rel="stylesheet" href="https://fonts.googleapis.com/css2?family=Jost:wght@300;400&display=swap">
<style>
  :root {
    --backdrop: #6b6b6b;
    --card: #ffffff;
    --dots: #f6e4e5;
    --blush: #f59296;
    --ink: #000000;
    --ring: #1a1a1a;
    --text: #1a1a1a;
  }
  html, body {
    margin: 0;
    width: 1200px;
    height: 1023px;
    overflow: hidden;
    background: var(--backdrop);
  }
  .stage {
    width: 1200px;
    height: 1023px;
    display: flex;
    flex-direction: column;
    align-items: center;
    justify-content: center;
    gap: 34px;
  }
  .business-card {
    position: relative;
    width: 800px;
    height: 457px;
    border-radius: 16px;
    overflow: hidden;
    box-shadow: 0 14px 32px rgba(0, 0, 0, 0.35);
    font-family: "Jost", sans-serif;
  }
  .card-front {
    background-color: var(--card);
    background-image: radial-gradient(var(--dots) 1.3px, transparent 1.6px);
    background-size: 26px 26px;
  }
  .card-back { background: var(--blush); }
  .corner-accent {
    position: absolute;
    inset: 0;
    width: 100%;
    height: 100%;
  }
  .corner-accent polygon { fill: var(--blush); }
  .emblem {
    position: absolute;
    left: 50%;
    top: 50%;
    width: 340px;
    height: 340px;
    transform: translate(-50%, -50%);
  }
  .emblem-ring { fill: none; stroke: var(--ring); stroke-width: 1.5; }
  .emblem-disk { fill: var(--ink); }
  .emblem-dot { fill: none; stroke: var(--blush); stroke-width: 3; }
  .brand-name {
    font-family: "Jost", sans-serif;
    font-weight: 300;
    font-size: 34px;
    letter-spacing: 3px;
    fill: var(--blush);
  }
  .contact {
    position: absolute;
    left: 430px;
    top: 110px;
    color: var(--text);
    font-weight: 300;
  }
  .contact-name {
    margin: 0 0 6px;
    font-size: 38px;
    font-weight: 300;
    letter-spacing: 1px;
  }
  .contact-role {
    margin: 0 0 34px;
    font-size: 17px;
    letter-spacing: 2px;
  }
  .contact-line {
    margin: 0 0 10px;
    font-size: 18px;
    letter-spacing: 0.5px;
  }
</style>
</head>
<body>
  <main class="stage">
    <section class="business-card card-front" aria-label="QM Interiors business card, front">
      <svg class="corner-accent" viewBox="0 0 800 457" preserveAspectRatio="none" aria-hidden="true">
        <polygon points="0,0 80,0 0,93"/>
        <polygon points="800,457 720,457 800,364"/>
      </svg>
      <svg class="emblem" viewBox="0 0 340 340">
        <circle class="emblem-ring" cx="170" cy="170" r="168"/>
        <circle class="emblem-disk" cx="170" cy="170" r="152"/>
        <circle class="emblem-dot" cx="170" cy="122" r="36"/>
        <text class="brand-name" x="170" y="222" text-anchor="middle">QM Interiors</text>
      </svg>
    </section>

    <section class="business-card card-back" aria-label="QM Interiors business card, back">
      <div class="contact">
        <p class="contact-name">Mara Quinn</p>
        <p class="contact-role">Design Consulting</p>
        <p class="contact-line">mara@qminteriors.com</p>
        <p class="contact-line">(555) 014-2290</p>
        <p class="contact-line">120 Alder Street, Portland</p>
      </div>
    </section>
  </main>
</body>
</html>
```